The Radiant Scroll of Petitions, Steadfast Petitions Across Seasons of Trial

I want a book cover design, The book is a prayer book. Pleas no design with only words. I want something creative and original. Something that attracts attention just by looking at the cover. Something powerful. This book is for people that are experiencing issues and need prayer. This book is also for those that want to pray and pray effectively. Not only will there be prayers. But they will learn the dynamics of prayer and how to pray effectively and from the right position. This book is filled with power yet effective prayers that will.have the ability to break bondages off people lives.
Below is some book covers that I found. I posted them to give an idea of what im looking for. Something that catches the attention of a reader.

Target Market(s)

Everyone, religious people

Industry/Entity Type

Religious

Font styles to use
Serif
Sans Serif

Requirements
Must have
• Creativity, originality,
Nice to have
• Professional looking. Powerful looking
Should not have
• Should not have just one color with big ole words across the whole book.

```html
<!DOCTYPE html>
<html lang="en">
<head>
<meta charset="utf-8">
<title>How to Pray — Book Cover</title>
<link rel="stylesheet" href="https://fonts.googleapis.com/css2?family=Noto+Sans:wght@400&family=Questrial&display=swap">
<style>
  :root {
    --page-bg: #f2f2f2;
    --cover-black: #0b0906;
    --cover-umber: #3a2e14;
    --glow-core: #fbecb8;
    --glow-mid: rgba(240, 220, 150, 0.55);
    --figure-violet: #9b88b5;
    --title-gold-light: #f2cf5a;
    --title-gold-dark: #9c7418;
    --subtitle-cream: #f3e2b8;
    --author-violet: #9d8ac0;
  }
  * { margin: 0; padding: 0; box-sizing: border-box; }
  html, body {
    width: 1200px;
    height: 1200px;
    overflow: hidden;
    background: var(--page-bg);
  }
  .stage {
    width: 1200px;
    height: 1200px;
    display: flex;
    align-items: center;
    justify-content: center;
  }
  .book-cover {
    position: relative;
    width: 733px;
    height: 1100px;
    overflow: hidden;
    background: var(--cover-black);
    box-shadow: 0 10px 40px rgba(0, 0, 0, 0.25);
  }
  .cover-pattern {
    position: absolute;
    inset: 0;
    background:
      radial-gradient(ellipse at 50% 40%, rgba(58, 46, 20, 0.9) 0%, rgba(30, 24, 10, 0.95) 45%, var(--cover-black) 100%);
  }
  .cover-glow {
    position: absolute;
    left: 381px;
    top: 420px;
    width: 640px;
    height: 640px;
    margin: -320px 0 0 -320px;
    border-radius: 50%;
    background: radial-gradient(circle, var(--glow-core) 0%, var(--glow-core) 30%, var(--glow-mid) 48%, rgba(200, 170, 90, 0.15) 62%, rgba(0, 0, 0, 0) 72%);
  }
  .cover-figure {
    position: absolute;
    left: 170px;
    top: 330px;
    width: 410px;
    height: 430px;
    border-radius: 46% 46% 40% 40%;
    background: radial-gradient(ellipse at 50% 50%, var(--figure-violet) 0%, var(--figure-violet) 45%, rgba(155, 136, 181, 0) 72%);
  }
  .title-block {
    position: absolute;
    inset: 0;
  }
  .title-kicker {
    position: absolute;
    left: 300px;
    top: 770px;
    font-family: "Noto Sans", sans-serif;
    font-size: 34px;
    letter-spacing: 1px;
    color: var(--subtitle-cream);
  }
  .title-main {
    position: absolute;
    left: 118px;
    top: 790px;
    font-family: "Questrial", sans-serif;
    font-size: 190px;
    line-height: 1;
    letter-spacing: 4px;
    background: linear-gradient(180deg, var(--title-gold-light) 0%, #d9a93a 45%, var(--title-gold-dark) 100%);
    -webkit-background-clip: text;
    background-clip: text;
    color: transparent;
  }
  .author-name {
    position: absolute;
    left: 280px;
    top: 975px;
    font-family: "Noto Sans", sans-serif;
    font-size: 34px;
    letter-spacing: 1px;
    color: var(--author-violet);
  }
</style>
</head>
<body>
  <main class="stage">
    <section class="book-cover">
      <div class="cover-pattern" role="img" aria-label="Dark ornamental lattice pattern in muted gold on black"></div>
      <div class="cover-glow"></div>
      <div class="cover-figure" role="img" aria-label="Violet silhouette of a person leaping joyfully with arms spread wide"></div>
      <div class="title-block">
        <p class="title-kicker">how to</p>
        <h1 class="title-main">PRAY</h1>
        <p class="author-name">Your Name</p>
      </div>
    </section>
  </main>
</body>
</html>
```